Marketing Flyer for Plumber Referals

8.5" x11" Layout should be landscape not portrait. Create a bold, eye-catching flyer that highlights earning potential from referrals for water damage restoration. Use high-contrast colors like blue, yellow, and white, with bold fonts and dynamic layouts. Include images of restoration work, cash, and happy clients. Emphasize key benefits like $500 minimum payouts, fast payments, and unlimited income potential. Keep instructions simple: refer a client, we handle the work, you get paid. Add a clear call-to-action and display contact details prominently. Focus on professionalism and energy.

Target Market(s)

Plumbers and Contractor 8.5" x11" Layout should be landscape not portrait.

Industry/Entity Type

General Contractor

Colors
0054AA
0677BA
7BADD7
CADEEF
E8F1F8
EB3D1F
EC4F4E
F09395
F8D3D4
FCEDEE

Requirements
Must have
• 8.5" x11" Layout should be landscape not portrait.
Nice to have

```html
<!DOCTYPE html>
<html lang="en">
<head>
<meta charset="utf-8">
<title>Referral Flyer – Front and Back</title>
<link rel="stylesheet" href="https://fonts.googleapis.com/css2?family=Poppins:wght@400;500;600;700;800;900&display=swap">
<style>
  :root{
    --navy:#14305a;
    --navy-deep:#0e2446;
    --blue:#0054AA;
    --blue-mid:#0677BA;
    --blue-soft:#7BADD7;
    --blue-pale:#CADEEF;
    --red:#EB3D1F;
    --red-soft:#EC4F4E;
    --yellow:#F6B21B;
    --white:#ffffff;
    --ink:#13223d;
    --grey:#d9dde3;
    --stage:#2b2b2b;
  }
  *{margin:0;padding:0;box-sizing:border-box}
  html,body{width:902px;height:1200px;overflow:hidden}
  body{background:var(--stage);font-family:"Poppins",sans-serif;position:relative}
  .card{position:absolute;width:636px;height:493px;overflow:hidden;background:var(--navy)}
  .card--front{left:60px;top:80px}
  .card--back{left:219px;top:636px}
  .abs{position:absolute}
  .placeholder{position:absolute}
  svg.shape{position:absolute;left:0;top:0}

  /* front */
  .front-kicker{left:26px;top:14px;font-size:39px;font-weight:800;color:var(--white);letter-spacing:.3px}
  .front-cash{left:22px;top:52px;font-size:124px;font-weight:800;color:var(--white);line-height:1;letter-spacing:-2px}
  .front-sub{left:28px;top:172px;font-size:23px;font-weight:700;color:var(--yellow)}
  .front-amount{left:24px;top:220px;font-size:84px;font-weight:800;color:var(--white);line-height:1;letter-spacing:-2px}
  .front-rate{left:258px;top:232px;font-size:19px;font-weight:700;color:var(--white);line-height:1.05}
  .front-partner{left:258px;top:280px;font-size:12px;font-weight:700;color:var(--navy-deep);line-height:1.1}
  .why-title{left:28px;top:340px;font-size:17px;font-weight:500;color:var(--white)}
  .benefits{left:28px;top:372px;width:400px;display:grid;grid-template-columns:205px 195px;row-gap:10px;list-style:none}
  .benefits li{position:relative;padding-left:12px;color:var(--white);font-size:7.5px;line-height:1.35}
  .benefits li::before{content:"";position:absolute;left:0;top:3px;width:4px;height:4px;border-radius:50%;background:var(--white)}
  .benefits strong{display:block;font-weight:600}
  .front-bar{left:0;top:458px;width:440px;height:35px;background:var(--yellow);padding:10px 0 0 40px;font-size:13.5px;font-weight:700;color:var(--ink)}
  .front-bar em{font-style:normal;color:var(--white)}

  /* back */
  .back-kicker{left:31px;top:44px;font-size:30px;font-weight:800;color:var(--white)}
  .back-flood{left:28px;top:78px;font-size:94px;font-weight:800;color:var(--white);line-height:1;letter-spacing:-1px}
  .how-title{left:48px;top:212px;font-size:27px;font-weight:400;color:var(--ink)}
  .steps{left:54px;top:258px;width:258px;list-style:none}
  .steps li{margin-bottom:10px;color:var(--white)}
  .steps .step-head{font-size:11.5px;font-weight:600}
  .steps .step-note{position:relative;padding-left:20px;font-size:8.5px;line-height:1.35;margin-top:3px}
  .steps .step-note::before{content:"";position:absolute;left:11px;top:4px;width:4px;height:4px;border-radius:50%;background:var(--white)}
  .flow-label{font-size:8px;font-weight:600;color:var(--ink);width:60px;text-align:center}
  .earn-mark{font-size:34px;font-weight:800;color:var(--yellow);width:56px;text-align:center;line-height:56px}
  .back-footer{left:0;top:414px;width:636px;height:79px}
  .cta-text{left:222px;top:432px;font-size:13.5px;font-weight:600;color:var(--ink);line-height:1.15}
  .cta-phone{left:380px;top:426px;font-size:26px;font-weight:800;color:var(--red)}
  .cta-web{left:380px;top:460px;font-size:14.5px;font-weight:500;color:var(--ink)}
  .sign-text{left:116px;top:432px;width:80px;text-align:center;font-size:11.5px;font-weight:800;color:var(--ink);line-height:1;letter-spacing:-.4px}
</style>
</head>
<body>

<section class="card card--front" aria-label="Flyer front">
  <div class="placeholder" role="img" aria-label="Faint currency banknote background texture" style="left:0;top:0;width:636px;height:220px;background:linear-gradient(135deg,#1b3a66,#142f57 60%,#1d3e6b)"></div>
  <div class="placeholder" role="img" aria-label="Flying dollar bills" style="left:405px;top:0;width:231px;height:228px;background:radial-gradient(ellipse at 50% 50%,#b8bfa6 0%,#7f8a73 45%,rgba(20,48,87,0) 72%)"></div>

  <svg class="shape" width="636" height="493" viewBox="0 0 636 493" aria-hidden="true">
    <path d="M0 322 L0 493 L636 493 L636 300 C520 330 300 300 0 322Z" fill="#1f4a7c"/>
    <path d="M0 232 C200 205 430 195 636 205 L636 300 C470 335 260 310 0 326Z" fill="var(--red)"/>
    <path d="M430 320 C520 320 590 305 636 296 L636 493 L430 493Z" fill="var(--blue-mid)"/>
  </svg>

  <div class="placeholder" role="img" aria-label="Smiling woman in a white shirt pointing upward" style="left:440px;top:222px;width:178px;height:271px;background:linear-gradient(180deg,#8a6a52,#e9e6e1 55%,#f4f2ef)"></div>

  <p class="abs front-kicker">EARN UNLIMITED</p>
  <p class="abs front-cash">CASH</p>
  <p class="abs front-sub">GET PAID TO REFER A FLOOD</p>
  <p class="abs front-amount">$500</p>
  <p class="abs front-rate">Minimum<br>or 10% Per Referral!</p>
  <p class="abs front-partner">Partner with the #1<br>Water Damage Restoration Team</p>

  <h2 class="abs why-title">Why Partner with Us?</h2>
  <ul class="abs benefits">
    <li><strong>Guaranteed Payout:</strong>Minimum $500 or 10% of the invoice, paid fast.</li>
    <li><strong>Industry Leaders:</strong>Certified experts with 24/7 rapid response.</li>
    <li><strong>Free Evaluations:</strong>We assess damage and process insurance claims for your clients.</li>
    <li><strong>Affordable Solutions:</strong>Lowest out-of-pocket costs for your customers.</li>
  </ul>

  <p class="abs front-bar">Send <em>Referrals</em>. Get <em>Paid</em>. Grow <em>Your Business</em>.</p>
</section>

<section class="card card--back" aria-label="Flyer back">
  <div class="placeholder" role="img" aria-label="Flooded home interior with staircase" style="left:0;top:0;width:636px;height:210px;background:linear-gradient(180deg,#2a4a72,#1a355f 60%,#13305a)"></div>
  <div class="placeholder" role="img" aria-label="Scattered gold coins" style="left:443px;top:8px;width:165px;height:88px;background:radial-gradient(ellipse at 50% 50%,#e2a83a 0%,#b8862e 40%,rgba(26,53,95,0) 72%)"></div>
  <div class="placeholder" role="img" aria-label="Hand writing the word referrals with a marker" style="left:422px;top:105px;width:174px;height:103px;background:linear-gradient(135deg,rgba(123,173,215,.35),rgba(232,200,180,.55))"></div>

  <svg class="shape" width="636" height="493" viewBox="0 0 636 493" aria-hidden="true">
    <path d="M0 212 C150 185 420 175 636 198 L636 493 L0 493Z" fill="var(--red)"/>
  </svg>

  <div class="placeholder" role="img" aria-label="Thoughtful woman in a beige blazer" style="left:490px;top:212px;width:146px;height:202px;background:linear-gradient(180deg,#3b2a24,#d9b7a2 45%,#e6d6c5)"></div>

  <svg class="shape" width="636" height="493" viewBox="0 0 636 493" aria-hidden="true">
    <circle cx="367" cy="251" r="31" fill="var(--white)" stroke="#f3b8a8" stroke-width="3"/>
    <circle cx="367" cy="251" r="24" fill="#7f93a8"/>
    <circle cx="445" cy="309" r="31" fill="var(--white)" stroke="#f3b8a8" stroke-width="3"/>
    <circle cx="445" cy="309" r="24" fill="#6fb5cf"/>
    <circle cx="367" cy="366" r="31" fill="var(--white)" stroke="#f3b8a8" stroke-width="3"/>
    <path d="M398 256 L432 283" stroke="var(--white)" stroke-width="2" fill="none"/>
    <path d="M426 281 L434 285 L430 277" stroke="var(--white)" stroke-width="2" fill="none"/>
    <path d="M432 333 L398 360" stroke="var(--white)" stroke-width="2" fill="none"/>
    <path d="M403 354 L396 362 L406 361" stroke="var(--white)" stroke-width="2" fill="none"/>
  </svg>

  <div class="placeholder back-footer" role="img" aria-label="Grey city skyline" style="background:linear-gradient(180deg,#e9ebee,#c9cdd3)"></div>
  <svg class="shape" width="636" height="493" viewBox="0 0 636 493" aria-hidden="true">
    <line x1="156" y1="446" x2="156" y2="493" stroke="#666" stroke-width="3"/>
    <path d="M156 401 L200 445 L156 489 L112 445Z" fill="#f7d21a" stroke="var(--ink)" stroke-width="2.5"/>
    <path d="M354 431 a4 4 0 0 1 4-4 l3 0 l2 5 l-2 2 a10 10 0 0 0 5 5 l2-2 l5 2 l0 3 a4 4 0 0 1-4 4 a15 15 0 0 1-15-15Z" fill="var(--ink)"/>
    <circle cx="363" cy="468" r="5.5" fill="none" stroke="var(--ink)" stroke-width="1.3"/>
    <ellipse cx="363" cy="468" rx="2.4" ry="5.5" fill="none" stroke="var(--ink)" stroke-width="1"/>
    <line x1="357.5" y1="468" x2="368.5" y2="468" stroke="var(--ink)" stroke-width="1"/>
  </svg>

  <p class="abs back-kicker">GET PAID TO REFER A</p>
  <p class="abs back-flood">FLOOD</p>

  <h2 class="abs how-title">How It Works</h2>
  <ol class="abs steps">
    <li><p class="step-head">1. Refer Flood, Water and Mold Damage</p><p class="step-note">Call, book online, or text us directly.</p></li>
    <li><p class="step-head">2. We Take Care of Everything</p><p class="step-note">Free evaluations, insurance claims, and professional service.</p></li>
    <li><p class="step-head">3. Get Paid Fast</p><p class="step-note">$500 minimum or 10% of the invoice within 48 hours of final payment.</p></li>
  </ol>

  <p class="abs flow-label" style="left:337px;top:287px">JOIN</p>
  <p class="abs flow-label" style="left:415px;top:345px">PROMOTE</p>
  <p class="abs earn-mark" style="left:339px;top:338px">$</p>
  <p class="abs flow-label" style="left:337px;top:402px">EARN</p>

  <p class="abs sign-text">GET PAID<br>TO SHARE</p>
  <p class="abs cta-text">Call Text or<br>Book On-line</p>
  <p class="abs cta-phone">555-014-2277</p>
  <p class="abs cta-web">HarborlineRestore.com</p>
</section>

</body>
</html>
```